Business cards

We need business cards for the logo that you designed for our company. Something simple and clean.

Target Market(s)

Homeowners/ people looking for construction work

Industry/Entity Type

Construction

Contact Information for Business Card

Name: Doug Whitby, Number: 602-555-0174, Email: WhitbyBuildingCompany@mailbox-example.net ROC# 482063

Font styles to use
Serif

Colors

Designer to choose colors to be used in the design.

Requirements
Must have
• On one side of the card I would like to be all of the personal information I have put above along with the company logo that I have attached.
• On the other side of the card I would like the top half of the card to be the logo and then on the bottom half I would like to have the areas of construction we focus on along with an icon that represents it like the picture I have attached.
• Areas we focus on:
• Roofing, Kitchen and bath Remodel, Water Damage, Storm Damage, Fire Damage, Insurance Specialist
• If we could arrange those in alphabetical order.
Nice to have
• I have added 2 company logos a colorful one and a black one it would be nice to see a couple different options the black logo to be more simple and sleek and the colorful logo to be more colorful

```html
<!DOCTYPE html>
<html lang="en">
<head>
<meta charset="utf-8">
<title>Whitby Building Company – Business Cards</title>
<link rel="stylesheet" href="https://fonts.googleapis.com/css2?family=Jost:wght@400;500&family=Oswald:wght@500&display=swap">
<style>
  :root {
    --brand-red: #cc2229;
    --brand-blue: #5fa3d6;
    --card-white: #ffffff;
    --page-bg: #ffffff;
    --card-edge: #d9d9d9;
  }
  * { box-sizing: border-box; margin: 0; padding: 0; }
  html, body {
    width: 1200px;
    height: 1200px;
    overflow: hidden;
    background: var(--page-bg);
    font-family: "Jost", "Helvetica Neue", Arial, sans-serif;
  }
  .card {
    position: absolute;
    width: 706px;
    height: 414px;
    background: var(--card-white);
    border: 1px solid var(--card-edge);
    overflow: hidden;
  }
  .card--front { left: 248px; top: 146px; }
  .card--back  { left: 250px; top: 623px; }

  .company-name {
    position: absolute;
    color: var(--brand-blue);
    font-weight: 500;
    text-transform: uppercase;
    letter-spacing: 1px;
    white-space: nowrap;
    display: flex;
    align-items: center;
    gap: 12px;
    z-index: 2;
  }
  .company-name__square {
    display: inline-block;
    flex: none;
    background: var(--brand-red);
  }
  .card--front .company-name { left: 58px; top: 86px; font-size: 24px; }
  .card--front .company-name__square { width: 30px; height: 30px; }
  .card--back .company-name {
    left: 0; right: 0; top: 86px;
    justify-content: center;
    font-size: 38px;
    letter-spacing: 1.5px;
    gap: 14px;
  }
  .card--back .company-name__square { width: 44px; height: 44px; }

  .name-band {
    position: absolute;
    left: 0; top: 204px;
    width: 470px; height: 60px;
  }
  .name-band__shape { position: absolute; inset: 0; }
  .holder-name {
    position: absolute;
    left: 58px; top: 10px;
    color: var(--card-white);
    font-size: 31px;
    font-weight: 500;
    line-height: 40px;
  }

  .contact-list {
    position: absolute;
    left: 58px; top: 277px;
    list-style: none;
    z-index: 2;
  }
  .contact-list__item {
    display: flex;
    align-items: center;
    gap: 8px;
    height: 35px;
    font-size: 18px;
    color: var(--brand-blue);
    white-space: nowrap;
  }
  .contact-list__icon { width: 14px; height: 16px; flex: none; }
  .contact-list__accent { color: var(--brand-red); }

  .brand-decoration {
    position: absolute;
    right: 0; top: 0;
    width: 264px; height: 414px;
  }

  .services {
    position: absolute;
    left: 0; top: 196px;
    width: 706px; height: 200px;
  }
  .services__label {
    font-family: "Oswald", "Arial Narrow", sans-serif;
    font-weight: 500;
    font-size: 17px;
    fill: var(--brand-red);
    text-anchor: middle;
  }
</style>
</head>
<body>

<section class="card card--front" aria-label="Business card front">
  <div class="company-name"><span class="company-name__square"></span>Whitby Building Company</div>

  <div class="name-band">
    <svg class="name-band__shape" viewBox="0 0 470 60" preserveAspectRatio="none" aria-hidden="true">
      <polygon points="0,0 424,0 470,60 0,60" fill="var(--brand-red)"/>
    </svg>
    <h1 class="holder-name">Doug Whitby</h1>
  </div>

  <ul class="contact-list">
    <li class="contact-list__item">
      <svg class="contact-list__icon" viewBox="0 0 14 16" aria-hidden="true">
        <path d="M3 1 L5.5 1 L6.5 5 L4.8 6.3 Q6 9.5 8.8 11 L10.2 9.4 L13.5 10.6 L13.2 13.6 Q12.6 15 10.8 14.8 Q3 13 1.2 3.6 Q1.2 1.4 3 1 Z" fill="var(--brand-red)"/>
      </svg>
      602-555-0174
    </li>
    <li class="contact-list__item">
      <svg class="contact-list__icon" viewBox="0 0 14 16" aria-hidden="true">
        <rect x="0.5" y="3.5" width="13" height="9" fill="var(--brand-red)"/>
        <polyline points="0.8,3.8 7,9 13.2,3.8" fill="none" stroke="#fff" stroke-width="1.2"/>
      </svg>
      <span>WhitbyBuildingCompany<span class="contact-list__accent">@mailbox-example.net</span></span>
    </li>
    <li class="contact-list__item">
      <svg class="contact-list__icon" viewBox="0 0 14 16" aria-hidden="true">
        <path d="M7 0.5 A5.5 5.5 0 0 1 12.5 6 Q12.5 9.5 7 15.5 Q1.5 9.5 1.5 6 A5.5 5.5 0 0 1 7 0.5 Z" fill="var(--brand-red)"/>
        <circle cx="7" cy="6" r="2.2" fill="#fff"/>
      </svg>
      ROC# 482063
    </li>
  </ul>

  <svg class="brand-decoration" role="img" aria-label="Large brand graphic in red and blue" viewBox="0 0 264 414" preserveAspectRatio="none">
    <defs>
      <linearGradient id="decorationTone" x1="0" y1="1" x2="1" y2="0">
        <stop offset="0" stop-color="#5fa3d6"/>
        <stop offset="1" stop-color="#cc2229"/>
      </linearGradient>
    </defs>
    <polygon points="124,0 264,0 264,414 24,414" fill="url(#decorationTone)" opacity="0.85"/>
  </svg>
</section>

<section class="card card--back" aria-label="Business card back">
  <div class="company-name"><span class="company-name__square"></span>Whitby Building Company</div>

  <svg class="services" viewBox="0 0 706 200" aria-label="Services">
    <rect x="0" y="18" width="706" height="88" fill="var(--brand-red)"/>
    <defs>
      <g id="pin">
        <path d="M-46,0 A46,46 0 1 1 46,0 Q44,22 0,63 Q-44,22 -46,0 Z" fill="var(--brand-blue)"/>
        <circle r="38" fill="#fff"/>
      </g>
    </defs>

    <g transform="translate(72,52)">
      <use href="#pin"/>
      <polyline points="-24,8 0,-14 24,8" fill="none" stroke="var(--brand-red)" stroke-width="4" stroke-linejoin="round"/>
      <rect x="11" y="-14" width="5" height="10" fill="var(--brand-red)"/>
    </g>
    <g transform="translate(182,52)" fill="none" stroke="var(--brand-red)" stroke-width="3">
      <use href="#pin" stroke="none"/>
      <rect x="-18" y="-10" width="24" height="24"/>
      <line x1="-18" y1="-3" x2="6" y2="-3"/>
      <rect x="-12" y="2" width="12" height="7"/>
      <path d="M8,0 Q20,0 20,-10 M20,-10 L20,-16"/>
      <circle cx="-10" cy="-16" r="3" fill="var(--brand-red)" stroke="none"/>
    </g>
    <g transform="translate(294,52)" fill="var(--brand-red)">
      <use href="#pin"/>
      <path d="M-6,-20 Q-20,0 -17,8 A11,11 0 0 0 5,8 Q8,0 -6,-20 Z"/>
      <path d="M11,-8 Q2,4 4,10 A8,8 0 0 0 18,10 Q20,4 11,-8 Z"/>
    </g>
    <g transform="translate(405,52)" fill="var(--brand-red)">
      <use href="#pin"/>
      <path d="M-20,4 A9,9 0 0 1 -14,-10 A12,12 0 0 1 8,-14 A10,10 0 0 1 20,4 Z"/>
      <polygon points="-2,6 6,6 1,14 7,14 -5,28 -1,17 -6,17"/>
    </g>
    <g transform="translate(517,52)" fill="var(--brand-red)">
      <use href="#pin"/>
      <path d="M2,-24 Q18,-6 14,8 A14,14 0 0 1 -14,8 Q-16,-2 -8,-10 Q-6,-2 -2,0 Q-4,-14 2,-24 Z"/>
      <path d="M0,0 Q8,8 5,14 A5,5 0 0 1 -5,14 Q-5,8 0,0 Z" fill="#fff"/>
    </g>
    <g transform="translate(629,52)">
      <use href="#pin"/>
      <path d="M0,-22 L19,-15 Q19,12 0,22 Q-19,12 -19,-15 Z" fill="var(--brand-red)"/>
      <path d="M0,-16 L0,16 Q-14,8 -14,-11 Z M0,0 L14,0 L14,-11 L0,-16 Z" fill="#fff" opacity="0.9"/>
    </g>

    <text class="services__label" x="72" y="140">Roofing</text>
    <text class="services__label" x="182" y="140">Kitchen&amp;Bath</text>
    <text class="services__label" x="182" y="159">Remodel</text>
    <text class="services__label" x="294" y="140">Water</text>
    <text class="services__label" x="294" y="159">Damage</text>
    <text class="services__label" x="405" y="140">Storm</text>
    <text class="services__label" x="405" y="159">Damage</text>
    <text class="services__label" x="517" y="140">Fire</text>
    <text class="services__label" x="517" y="159">Damage</text>
    <text class="services__label" x="629" y="140">Insurance</text>
    <text class="services__label" x="629" y="159">Specialist</text>
  </svg>
</section>

</body>
</html>
```